Fertility consulting business needs oversized postcard handout

We need an oversized postcard that we can hand out and leave around in many places. It needs to be an overview of our business and get people to go to the website to sign up for a class.

I am including exact verbiage in "Must Haves" section.
Colors used should be colors from logo. And website: www.lunabloomcycles.com Or, a brown base, with colors from logo. Will send a scan of business card that is set up this way.
Two-sided.
Will print with Prentora

Target Market(s)

women

Industry/Entity Type

Business

Font styles to use
Sans Serif
Script

Requirements
Must have
• FRONT:
• logo
• The TRUTH every woman deserves to know about her fertility.
• The Halvery Method is a system of fertility awareness education. Women and couples can fully understand their own fertility to avoid or achieve pregnancy or monitor reproductive health.
• In San Diego County and online instruction available
• Contact us at: www.lunabloomcycles.com | 619.482.5173 | www.circlewall.com/lunabloomcycles
• ON BACK:
• Learning the Halvery Method provides access to real women's healthcare and help for: [I WILL PROVIDE A LIST]
• - help for breastfeeding and coming off of hormonal birth control
• - daily observation of biomarkers and charting
• - one-on-one confidential instruction
• - 100% natural, 99.6% effective to avoid pregnancy, 75% effective to achieve pregnancy in one cycle
Nice to have
• Incorporate the photo that I will send - showing me working with a client.
Should not have
• Pictures of men.

```html
<!DOCTYPE html>
<html lang="en">
<head>
<meta charset="utf-8">
<title>Luna Bloom Cycles – Postcard</title>
<link rel="stylesheet" href="https://fonts.googleapis.com/css2?family=Oswald:wght@500&family=Montserrat:wght@500;600&family=Roboto:wght@400;500&display=swap">
<style>
  :root {
    --page: #dcdcdf;
    --maroon: #5e1610;
    --brick: #a8321d;
    --ember: #d2452a;
    --olive: #c3bf55;
    --pink: #e5699a;
    --sage: #c8d6a4;
    --paper: #ffffff;
    --panel: #f7f8f7;
    --ink: #3a3a3a;
    --rule: #6d6d6d;
  }
  * { box-sizing: border-box; margin: 0; padding: 0; }
  html, body { width: 1200px; height: 1200px; overflow: hidden; }
  body { background: var(--page); position: relative; font-family: "Montserrat", sans-serif; }

  .card { position: absolute; left: 205px; width: 790px; height: 512px; overflow: hidden; }
  .card--front { top: 66px; background: radial-gradient(ellipse 60% 70% at 45% 45%, var(--ember), var(--brick) 55%, var(--maroon)); }
  .card--back { top: 603px; background: var(--paper); }

  .band { position: absolute; bottom: 0; height: 22px; }
  .band--olive { left: 0; background: var(--olive); }
  .band--pink { right: 0; background: var(--pink); }

  .headline { position: absolute; font-family: "Oswald", sans-serif; font-weight: 500; text-transform: uppercase; letter-spacing: -0.3px; }
  .card--front .headline { left: 35px; top: 30px; width: 300px; color: var(--olive); font-size: 32px; line-height: 38px; }
  .intro { position: absolute; left: 35px; top: 192px; width: 300px; color: #fff; font-size: 10.4px; line-height: 14px; font-weight: 500; }
  .area { position: absolute; left: 35px; top: 262px; color: #fff; font-size: 11.5px; line-height: 16px; font-weight: 500; text-transform: uppercase; }

  .brand { position: absolute; display: flex; flex-direction: column; align-items: center; gap: 8px; font-family: "Montserrat", sans-serif; font-weight: 600; color: var(--pink); text-align: center; }
  .brand__dot { width: 34px; height: 34px; border-radius: 50%; background: var(--olive); }
  .brand__name { font-size: 20px; line-height: 23px; white-space: nowrap; }
  .card--front .brand { left: 16px; top: 350px; width: 150px; }
  .card--back .brand { left: 385px; top: 22px; width: 150px; }
  .card--back .brand__name { font-size: 19px; line-height: 21px; }

  .contact { position: absolute; }
  .contact__kicker { font-size: 10px; font-weight: 500; line-height: 12px; }
  .contact__title { font-size: 19px; font-weight: 600; line-height: 22px; text-decoration: underline; text-underline-offset: 3px; text-decoration-thickness: 2px; }
  .contact__list { list-style: none; margin-top: 16px; }
  .contact__list li { display: flex; align-items: center; height: 29px; font-size: 12px; font-weight: 500; letter-spacing: 0.2px; white-space: nowrap; }
  .contact__list svg { width: 18px; height: 18px; margin-right: 16px; flex: none; }
  .card--front .contact { left: 176px; top: 347px; color: #fff; }
  .card--front .contact__kicker { color: #fff; }
  .card--front .contact__title { color: var(--olive); }
  .card--front .contact__list svg { color: var(--olive); }
  .card--back .contact { left: 48px; top: 338px; color: var(--ink); }
  .card--back .contact__kicker, .card--back .contact__title, .card--back .contact__list svg { color: var(--pink); }
  .card--back .contact__list { margin-top: 12px; }

  .photos { position: absolute; inset: 0; width: 790px; height: 512px; }

  .back-panel { position: absolute; left: 0; top: 0; width: 378px; height: 490px; background: var(--panel); }
  .card--back .headline { left: 36px; top: 38px; width: 350px; color: var(--pink); font-size: 20px; line-height: 27px; letter-spacing: -0.6px; }
  .benefits { position: absolute; left: 48px; top: 142px; width: 320px; list-style: none; }
  .benefits li { display: flex; font-family: "Roboto", sans-serif; font-size: 11.3px; line-height: 17px; color: var(--ink); margin-bottom: 10px; }
  .benefits svg { width: 15px; height: 15px; margin: 1px 12px 0 0; flex: none; color: var(--pink); }

  .indicia { position: absolute; left: 675px; top: 19px; width: 94px; height: 94px; border: 1.5px solid #111; font-family: "Roboto", sans-serif; font-size: 11px; line-height: 13px; color: #111; text-align: center; padding-top: 9px; }
  .indicia strong { font-weight: 500; }
  .address-line { position: absolute; left: 410px; width: 341px; height: 1px; background: var(--rule); }
</style>
</head>
<body>

<section class="card card--front" aria-label="Postcard front">
  <svg class="photos" viewBox="0 0 790 512">
    <defs>
      <clipPath id="clip-main"><circle cx="604" cy="166" r="263"/></clipPath>
      <linearGradient id="tone-room" x1="0" y1="0" x2="1" y2="1">
        <stop offset="0" stop-color="#e6ece6"/><stop offset="0.5" stop-color="#cfd4c4"/><stop offset="1" stop-color="#8f7f70"/>
      </linearGradient>
      <linearGradient id="tone-mother" x1="0" y1="0" x2="1" y2="1">
        <stop offset="0" stop-color="#f4ece6"/><stop offset="1" stop-color="#d9b6a0"/>
      </linearGradient>
      <linearGradient id="tone-family" x1="0" y1="0" x2="1" y2="1">
        <stop offset="0" stop-color="#6a4a3a"/><stop offset="1" stop-color="#f1e5b8"/>
      </linearGradient>
    </defs>
    <circle cx="604" cy="166" r="268" fill="var(--olive)"/>
    <rect x="0" y="0" width="790" height="512" fill="url(#tone-room)" clip-path="url(#clip-main)" role="img" aria-label="Photo: a fertility educator talking with a client in a bright sitting room"/>
    <circle cx="445" cy="341" r="68" fill="var(--pink)"/>
    <circle cx="445" cy="341" r="56" fill="url(#tone-mother)" role="img" aria-label="Photo: a mother holding her newborn baby"/>
    <circle cx="607" cy="394" r="80" fill="var(--sage)"/>
    <circle cx="607" cy="394" r="67" fill="url(#tone-family)" role="img" aria-label="Photo: young parents smiling with their baby"/>
  </svg>

  <h1 class="headline">The truth every woman deserves to know about her fertility</h1>
  <p class="intro">The Halvery Method is a system of fertility awareness education. Women and couples can fully understand their own fertility to avoid or achieve pregnancy or monitor reproductive health.</p>
  <p class="area">In San Diego County and<br>online instruction available.</p>

  <div class="brand"><span class="brand__dot"></span><span class="brand__name">Luna Bloom<br>Cycles</span></div>

  <div class="contact">
    <p class="contact__kicker">GET IN</p>
    <p class="contact__title">TOUCH</p>
    <ul class="contact__list">
      <li><svg viewBox="0 0 24 24"><path fill="currentColor" d="M3 9c0-3 4-5 9-5s9 2 9 5v2h-5V9H8v2H3zM6 12h12l2 8H4z"/></svg>619.482.5173</li>
      <li><svg viewBox="0 0 24 24" fill="none" stroke="currentColor" stroke-width="1.8"><circle cx="12" cy="12" r="9"/><ellipse cx="12" cy="12" rx="4" ry="9"/><path d="M3 12h18M5 7h14M5 17h14"/></svg>www.lunabloomcycles.com</li>
      <li><svg viewBox="0 0 24 24"><circle cx="12" cy="12" r="6" fill="currentColor"/></svg>www.circlewall.com/lunabloomcycles</li>
    </ul>
  </div>

  <div class="band band--olive" style="width:334px"></div>
  <div class="band band--pink" style="width:456px"></div>
</section>

<section class="card card--back" aria-label="Postcard back">
  <div class="back-panel"></div>
  <h2 class="headline">Learning the Halvery Method provides access to real women's healthcare and help for:</h2>
  <ul class="benefits">
    <li><svg viewBox="0 0 24 24" fill="none" stroke="currentColor" stroke-width="2.4"><circle cx="12" cy="12" r="10"/><path d="M7.5 12.5l3 3 6-6"/></svg>Lorem Ipsum is simply ummy text of mmy text of etting indupends.</li>
    <li><svg viewBox="0 0 24 24" fill="none" stroke="currentColor" stroke-width="2.4"><circle cx="12" cy="12" r="10"/><path d="M7.5 12.5l3 3 6-6"/></svg>Lorem Ipsum is simply ummy text of mmy text of etting indupends.</li>
    <li><svg viewBox="0 0 24 24" fill="none" stroke="currentColor" stroke-width="2.4"><circle cx="12" cy="12" r="10"/><path d="M7.5 12.5l3 3 6-6"/></svg>Lorem Ipsum is simply ummy text of mmy text of etting indupends.</li>
  </ul>

  <div class="contact">
    <p class="contact__kicker">GET IN</p>
    <p class="contact__title">TOUCH</p>
    <ul class="contact__list">
      <li><svg viewBox="0 0 24 24"><path fill="currentColor" d="M3 9c0-3 4-5 9-5s9 2 9 5v2h-5V9H8v2H3zM6 12h12l2 8H4z"/></svg>619.482.5173</li>
      <li><svg viewBox="0 0 24 24" fill="none" stroke="currentColor" stroke-width="1.8"><circle cx="12" cy="12" r="9"/><ellipse cx="12" cy="12" rx="4" ry="9"/><path d="M3 12h18M5 7h14M5 17h14"/></svg>www.lunabloomcycles.com</li>
      <li><svg viewBox="0 0 24 24"><circle cx="12" cy="12" r="6" fill="currentColor"/></svg>www.circlewall.com/lunabloomcycles</li>
    </ul>
  </div>

  <div class="brand"><span class="brand__dot"></span><span class="brand__name">Luna Bloom<br>Cycles</span></div>

  <div class="indicia">PRESORTED<br>STANDARD<br>US POSTAGE<br><strong>PAID</strong><br>ALDERTON, OH<br>PERMIT #1005</div>

  <div class="address-line" style="top:223px"></div>
  <div class="address-line" style="top:290px"></div>
  <div class="address-line" style="top:358px"></div>
  <div class="address-line" style="top:425px"></div>

  <div class="band band--olive" style="width:378px"></div>
  <div class="band band--pink" style="width:412px"></div>
</section>

</body>
</html>
```